Website for new dental office

I am Dr. Colin Marsh and am building a new dental practice. I specialize in general dentistry. I am young and have a higher end dental practice incorporating very new technologies and would like my website to reflect that. As many dental patients are older, the website must be very easy to navigate. I would like patients to be able to request appointments, and will eventually add on patient information forms (the health history, etc, that you normally fill out in the practice) from my practice management software, so leave an area for that.

Industry/Entity Type

Building

```html
<!DOCTYPE html>
<html lang="en">
<head>
<meta charset="utf-8">
<title>Marsh Dental — Dental Services</title>
<link rel="stylesheet" href="https://fonts.googleapis.com/css2?family=Ubuntu:wght@400;500;700&family=Open+Sans:wght@400&family=PT+Sans:wght@700&display=swap">
<style>
:root{
  --blue:#3a8de4;
  --blue-line:#6aaaf0;
  --ink:#3c4650;
  --muted:#5d6670;
  --heading:#4b5a69;
  --hero-bg:#eef0f2;
  --footer:#4e5f72;
  --footer-dark:#4a5a6c;
  --footer-text:#e6ecf2;
  --link:#3a8de4;
  --rule:#dfe3e7;
  --white:#ffffff;
}
*{margin:0;padding:0;box-sizing:border-box}
html,body{width:1010px;height:1200px;overflow:hidden;background:var(--white)}
body{font-family:"Ubuntu",sans-serif;color:var(--ink);position:relative}
.abs{position:absolute}

/* hero */
.hero{left:0;top:0;width:1010px;height:501px;background:var(--hero-bg)}
.hero-photo{left:278px;top:76px;width:732px;height:368px;
  background:radial-gradient(ellipse at 55% 40%,#f3e3d4 0%,#e4e8ee 45%,#eef0f2 80%)}
.tool-tab{left:0;top:81px;width:24px;height:22px;background:var(--blue);border-radius:0 3px 3px 0}
.hero-title{left:92px;top:222px;font-family:"PT Sans",sans-serif;font-weight:700;font-size:33px;color:var(--heading);letter-spacing:.3px}
.play-box{left:86px;top:280px;width:66px;height:66px;border:2px solid #fff;border-radius:3px;background:rgba(255,255,255,.15)}
.play-box span{position:absolute;left:30px;top:27px;width:4px;height:10px;border-radius:2px;background:#a9c6e6}
.hero-dash{left:86px;top:375px;width:14px;height:2px;border-top:1px solid var(--blue-line);border-bottom:1px solid var(--blue-line)}
.hero-text{left:112px;top:368px;width:400px;font-size:11px;line-height:15px;color:var(--muted)}

/* header */
.site-header{left:69px;top:0;width:882px;height:60px;background:var(--white);box-shadow:0 1px 3px rgba(0,0,0,.2);border-radius:0 0 3px 3px}
.brand{left:24px;top:16px;font-size:22px;font-weight:500;color:#2d2d2d}
.nav{left:402px;top:24px;display:flex;gap:0;font-size:11px;color:#333}
.nav a{color:#333;text-decoration:none;position:absolute;white-space:nowrap}
.nav .current{color:var(--blue)}
.search{left:827px;top:21px}

/* appointment */
.appt{left:69px;top:444px;width:883px;height:216px;background:var(--blue);border-radius:0 0 3px 3px}
.appt-tab{left:0;top:0;width:396px;height:57px;font-size:14.5px;color:#fff;padding:20px 0 0 19px;font-weight:500}
.appt-emerg{left:396px;top:0;width:487px;height:57px;background:#fff;font-size:14.5px;color:#444;padding:20px 0 0 50px}
.appt-emerg svg{position:absolute;left:27px;top:19px}
.col-head{font-size:10.5px;color:#fff;text-transform:uppercase;font-weight:500;white-space:nowrap}
.col-head svg{position:absolute;left:-17px;top:0}
.hours{left:22px;top:110px;width:193px}
.hours .row{position:absolute;left:0;width:193px;height:30px;border-bottom:1px solid rgba(255,255,255,.75);font-size:10px;color:#fff;font-weight:500}
.hours .row span{position:absolute;top:8px}
.docs-text{left:238px;top:115px;width:192px;font-size:10px;line-height:15px;color:#fff;font-weight:500}
.btn-light{left:238px;top:166px;width:115px;height:25px;border-radius:13px;background:#fff;color:#777;font-size:11px;text-align:center;line-height:25px}
.field{height:20px;border:1px solid #fff;border-radius:11px;font-size:10px;color:#fff;padding:0 8px;line-height:18px}
.field-select svg{position:absolute;right:8px;top:7px}
.btn-send{height:21px;border-radius:11px;background:#fff;color:#888;font-size:10.5px;text-align:center;line-height:21px}

/* content */
.sec-title{font-size:14.5px;font-weight:500;color:#2c3640;letter-spacing:.3px}
.rule{height:1px;background:var(--rule)}
.rule-accent{height:2px;background:var(--blue-line)}
.photo{border-radius:2px}
.lorem{font-family:"Open Sans",sans-serif;font-size:9.7px;line-height:13.5px;color:#555}
.lorem p{margin-bottom:4px}
.card-label{position:absolute;left:0;bottom:12px;background:rgba(40,40,40,.8);color:#fff;font-family:"PT Sans",sans-serif;font-weight:700;font-size:12px;padding:5px 7px}
.card-text{font-size:10px;line-height:15.6px;color:#666;font-family:"Open Sans",sans-serif}
.arrows{left:912px;top:688px;color:#333;font-size:14px}

/* footer */
.footer{left:0;top:950px;width:1010px;height:250px;background:var(--footer);color:var(--footer-text)}
.foot-brand{left:56px;top:16px;font-size:22px;font-weight:500;color:#fff}
.foot-head{font-size:14.5px;color:#fff}
.foot-p{font-size:10.2px;line-height:13.5px;color:var(--footer-text)}
.news-title{font-size:10.5px;color:#fff;font-weight:500}
.news-date{font-size:8px;color:var(--footer-text)}
.social{font-size:10.5px;color:#fff}
.social i{position:absolute;left:-30px;top:-3px;width:19px;height:19px;border-radius:50%;background:#fff}
.foot-bar{left:0;top:210px;width:1010px;height:40px;border-top:1px solid #5f6f82;background:var(--footer-dark);font-size:9px;color:#fff}
.to-top{left:496px;top:14px;width:19px;height:19px;border:1px solid #cfd8e2;border-radius:2px}
</style>
</head>
<body>

<section class="hero abs">
  <div class="hero-photo abs" role="img" aria-label="Photo of a smiling team of dental doctors in white coats"></div>
  <div class="tool-tab abs"><svg width="24" height="22" viewBox="0 0 24 22"><path d="M6 17l3-1 8-9-2-2-8 9z" fill="#fff"/></svg></div>
  <h1 class="hero-title abs">Dental Services</h1>
  <div class="play-box abs"><span></span></div>
  <div class="hero-dash abs"></div>
  <p class="hero-text abs">More than 330 physicians, scientists and researchers, est etiam processus dynamicus, qui sequitur mutationem consuetudium lectorum.</p>
</section>

<header class="site-header abs">
  <div class="brand abs">Marsh Dental</div>
  <nav class="nav abs">
    <a class="current" style="left:0">Home</a>
    <a style="left:50px">About us</a>
    <a style="left:113px">Medical Services</a>
    <a style="left:213px">Departments</a>
    <a style="left:297px">Timetable</a>
    <a style="left:364px">Contact</a>
  </nav>
  <svg class="search abs" width="14" height="14" viewBox="0 0 14 14"><circle cx="5.5" cy="5.5" r="4.3" fill="none" stroke="#8cbdf0" stroke-width="1.4"/><path d="M8.7 8.7l4 4" stroke="#8cbdf0" stroke-width="1.6"/></svg>
</header>

<section class="appt abs">
  <div class="appt-tab abs">Make an Appointment</div>
  <div class="appt-emerg abs">
    <svg width="17" height="15" viewBox="0 0 17 15"><rect x="0" y="3" width="17" height="12" rx="2" fill="#555"/><rect x="5" y="0" width="7" height="4" rx="1" fill="none" stroke="#555" stroke-width="1.5"/><path d="M8.5 6v6M5.5 9h6" stroke="#fff" stroke-width="2"/></svg>
    For emergency cases →
  </div>

  <div class="col-head abs" style="left:40px;top:86px"><svg width="12" height="12" viewBox="0 0 12 12"><circle cx="6" cy="6" r="5" fill="none" stroke="#fff"/><path d="M6 3v3h2.5" stroke="#fff" fill="none"/></svg>Working time</div>
  <div class="hours abs">
    <div class="row" style="top:-8px"><span style="left:0">Monday – Friday</span><span style="left:104px">–</span><span style="left:135px">8.00 – 17.00</span></div>
    <div class="row" style="top:22px"><span style="left:0">Saturday</span><span style="left:104px">–</span><span style="left:135px">9.30 – 17.30</span></div>
    <div class="row" style="top:52px"><span style="left:0">Sunday</span><span style="left:104px">–</span><span style="left:135px">9.30 – 15.00</span></div>
  </div>

  <div class="col-head abs" style="left:255px;top:86px"><svg width="12" height="12" viewBox="0 0 12 12"><rect x="1" y="2" width="10" height="9" fill="none" stroke="#fff"/><path d="M1 5h10M4 7h1M7 7h1M4 9h1M7 9h1" stroke="#fff"/></svg>Doctors timetable</div>
  <p class="docs-text abs">Claritas est etiam processus dynamicus, qui sequitur mutationem consuetudium lectorum.</p>
  <div class="btn-light abs">View Timetable →</div>

  <div class="col-head abs" style="left:470px;top:86px"><svg width="12" height="12" viewBox="0 0 12 12"><rect x="3" y="1" width="6" height="10" rx="3" fill="none" stroke="#fff"/></svg>Booking a visit</div>
  <div class="field field-select abs" style="left:453px;top:110px;width:193px">Select departments:<svg width="8" height="5" viewBox="0 0 8 5"><path d="M0 0h8L4 5z" fill="#fff"/></svg></div>
  <div class="field abs" style="left:669px;top:110px;width:186px">Your phone</div>
  <div class="field abs" style="left:453px;top:142px;width:193px;height:21px">Full name</div>
  <div class="field abs" style="left:669px;top:142px;width:106px;height:21px">dd/mm/yyyy</div>
  <div class="btn-send abs" style="left:797px;top:142px;width:63px">Send →</div>
</section>

<section class="welcome">
  <h2 class="sec-title abs" style="left:71px;top:690px">WELCOMER</h2>
  <div class="rule abs" style="left:69px;top:711px;width:413px"></div>
  <div class="rule-accent abs" style="left:69px;top:710px;width:101px"></div>
  <div class="photo abs" style="left:75px;top:733px;width:98px;height:98px;background:linear-gradient(135deg,#6fa8d8,#d9e6f1 60%,#3b7fc0)" role="img" aria-label="Photo of a doctor's desk with a stethoscope"></div>
  <div class="lorem abs" style="left:193px;top:732px;width:266px">
    <p>Lorem ipsum dolor sit amet, consectetuer fdadpiscing sed diam nonummy nibh euismod tincilt ut laoreet dor Lorem ipsum dolor sit amet, consectetuer hkkd; ght fdadpiscing sed diam nonummy dor.</p>
    <p>Lorem ipsum dolor sit amet, consectetuer fdadpiscing ds sed diam nonummy nibhf feuismod tincilt ut laoreet dor Lorem ipsum dolor sit amet.</p>
  </div>
  <div class="lorem abs" style="left:74px;top:842px;width:392px">
    <p>Lorem ipsum dolor sit amet, consectetuer fdadpiscing sed diam nonummy nibh sd tincilt ut fgwhy a fhkkd; ght laoreet dor Lorem ipsum dolor sit amet, consectetuer fdadpiscing sed diam nonummy nibhfg sd euismod tincilt ut laoreet dor.</p>
    <p>Lorem ipsum dolor sit amet, consectetuer fdadpiscing sed diam nonummy nibh s euismod tincilt dor Lorem ipsum dolor sit amet.</p>
  </div>
</section>

<section class="services">
  <h2 class="sec-title abs" style="left:514px;top:690px">OUR SERVICES</h2>
  <div class="arrows abs">‹ &nbsp;›</div>
  <div class="rule abs" style="left:514px;top:711px;width:440px"></div>
  <div class="rule-accent abs" style="left:514px;top:710px;width:100px"></div>
  <div class="rule-accent abs" style="left:656px;top:710px;width:99px"></div>

  <div class="photo abs" style="left:514px;top:735px;width:202px;height:140px;background:linear-gradient(160deg,#5a8fb0,#b9c9d4 55%,#c98f86)" role="img" aria-label="Photo of a dentist treating a young patient">
    <span class="card-label">Dental Crown</span>
  </div>
  <p class="card-text abs" style="left:514px;top:883px;width:205px">Duis mollis, est non commodo luctus, nisi erat porttitor ligula, eget lacinia odio sem nec elit. Cras mattis consectetur</p>

  <div class="photo abs" style="left:739px;top:735px;width:202px;height:140px;background:linear-gradient(160deg,#dfe4e8,#c6ccd2 50%,#b7c94a)" role="img" aria-label="Photo of a dentist examining a smiling patient in the chair">
    <span class="card-label">Dantal Filling</span>
  </div>
  <p class="card-text abs" style="left:739px;top:883px;width:205px">Duis mollis, est non commodo luctus, nisi erat porttitor ligula, eget lacinia odio sem nec elit. Cras mattis consectetur</p>
</section>

<footer class="footer abs">
  <div class="foot-brand abs">Marsh Dental</div>
  <p class="foot-p abs" style="left:56px;top:64px;width:200px">Claritas est etiam processus dynamicus, qui sequitur mutationem consuetudium lectorum.</p>
  <p class="foot-p abs" style="left:56px;top:116px;width:200px">Claritas est etiam processus dynamicus, qui sequitur mutationem consuetudium lectorum.</p>

  <h3 class="foot-head abs" style="left:291px;top:20px;font-weight:400">Latest news &amp; tips</h3>
  <div class="abs" style="left:291px;top:65px"><div class="news-title">The face you will remember</div><div class="news-date">June 22, 2013</div></div>
  <div class="abs" style="left:291px;top:98px"><div class="news-title">This is a healthy gallery</div><div class="news-date">September 10, 2013</div></div>
  <div class="abs" style="left:291px;top:131px"><div class="news-title">Aurelio spring collection 2009</div><div class="news-date">July 27, 2013</div></div>

  <h3 class="foot-head abs" style="left:528px;top:20px;font-weight:400">Contact us</h3>
  <p class="foot-p abs" style="left:528px;top:64px;width:200px;line-height:15px">Sundays @ 10:00a<br>London, UK<br>24, Elm Row, Harrow Vale,</p>
  <p class="foot-p abs" style="left:528px;top:115px;width:220px;line-height:15px">Tel: 02 481-337<br>Mobile: 02 481-33<br>E-mail: <span style="color:#fff;font-weight:500">hello@marshdental-care.com</span></p>
  <p class="foot-p abs" style="left:528px;top:175px;color:var(--link)">Get directions on the map →</p>

  <h3 class="foot-head abs" style="left:764px;top:20px;font-weight:400">Stay Connected</h3>
  <div class="social abs" style="left:797px;top:68px"><i></i>Friendlink</div>
  <div class="social abs" style="left:797px;top:100px"><i></i>Chirpline</div>
  <div class="social abs" style="left:797px;top:131px"><i></i>Circles+</div>
  <div class="social abs" style="left:797px;top:163px"><i></i>Pinboard</div>

  <div class="foot-bar abs">
    <span class="abs" style="left:33px;top:13px">2014 © Copyright - Marsh Dental</span>
    <div class="to-top abs"><svg width="17" height="17" viewBox="0 0 17 17"><path d="M8.5 5v8M6.5 7l2-2 2 2" stroke="#fff" fill="none"/></svg></div>
    <span class="abs" style="left:791px;top:14px">For emergency cases</span>
    <svg class="abs" style="left:889px;top:12px" width="12" height="12" viewBox="0 0 12 12"><path d="M2 1l2 0 1 3-1.5 1a7 7 0 0 0 3.5 3.5L8 7l3 1v2a1 1 0 0 1-1 1A9 9 0 0 1 1 2a1 1 0 0 1 1-1z" fill="#cfe0f2"/></svg>
    <span class="abs" style="left:910px;top:14px;color:#e6ecf2">1-800-555-0142</span>
  </div>
</footer>

</body>
</html>
```